Poster design for a vet clinic

Running a campaign called 'Pal Spotter', which is where people get a $30 voucher for themselves and their friend if they refer somebody to our vet clinic.

Text something like:
We love Pal Spotters!
Refer a fur friend to our friendly team and both your fur child and their fur child will receive a $30 voucher to use in clinic! *
* Limited to one pet per fur parent and the referred fur parent must be new to our clinic. Unlimited vouchers for number of referrals!

I want it to be cute but professional. You can see the design styles at vettoly.com.au/northryde and see the logo there too.
I am thinking of having a dog whispering to a cat or something like that as the main image.
I would like both the photoshop file and the pdf please. Would be for an A2 poster.

```html
<!DOCTYPE html>
<html lang="en">
<head>
<meta charset="utf-8">
<title>Pal Spotters – Vettoly Referral Poster</title>
<link rel="stylesheet" href="https://fonts.googleapis.com/css2?family=Fredoka:wght@600&family=Pacifico&family=Fira+Sans+Condensed:wght@600;700&family=Bree+Serif&display=swap">
<style>
  :root {
    --orange: #f07f22;
    --pink: #ec1c7a;
    --paw-pink: #f3c3c0;
    --brown: #6b4a3a;
    --teal: #1ba3aa;
    --paper: #f9f0ee;
    --yellow-light: #fdc832;
    --yellow-deep: #f6a41b;
    --white: #ffffff;
    --ink: #1d1d1d;
  }
  * { margin: 0; padding: 0; box-sizing: border-box; }
  html, body { width: 846px; height: 1200px; overflow: hidden; background: var(--white); }
  .poster { position: relative; width: 846px; height: 1200px; overflow: hidden; background: var(--white); }

  .hero-photo {
    position: absolute; left: 100px; top: 0; width: 690px; height: 330px;
    background: radial-gradient(ellipse at 35% 55%, #c98a4c 0%, #b27a45 30%, transparent 60%),
                radial-gradient(ellipse at 72% 45%, #c9c2ba 0%, #a99f95 35%, transparent 62%),
                linear-gradient(180deg, #f4f2ef, #e9e4de);
  }

  .paper { position: absolute; left: 0; top: 270px; width: 846px; height: 870px; }
  .paper svg { display: block; }

  .voucher-tag {
    position: absolute; left: 22px; top: 52px; width: 284px; height: 90px;
    transform: rotate(-9deg);
  }
  .voucher-tag .tag-frame {
    position: absolute; inset: 12px -10px -12px 12px; border: 3px solid var(--ink);
  }
  .voucher-tag .tag-body {
    position: absolute; inset: 0; background: var(--orange);
    display: flex; align-items: center; justify-content: center;
    font-family: "Fira Sans Condensed", sans-serif; font-weight: 700;
    font-size: 44px; color: var(--white); letter-spacing: 0.5px;
  }
  .voucher-tag sup { font-size: 22px; margin-right: 2px; }
  .tag-pets {
    position: absolute; left: 104px; top: -36px; width: 92px; height: 40px;
    background: var(--orange); border: 3px solid var(--brown);
    border-radius: 20px 20px 6px 6px;
  }

  .headline {
    position: absolute; left: 0; width: 846px; text-align: center;
    font-family: "Fredoka", sans-serif; font-weight: 600; color: var(--orange);
  }
  .headline-we { top: 362px; font-size: 72px; left: -68px; }
  .heart { position: absolute; left: 430px; top: 340px; width: 106px; height: 96px; }
  .headline-name { top: 426px; font-size: 76px; letter-spacing: 1px; }

  .offer-card {
    position: absolute; left: 75px; top: 530px; width: 697px; height: 330px;
    background: linear-gradient(160deg, var(--yellow-light) 0%, #fbb827 55%, var(--yellow-deep) 100%);
    box-shadow: 0 14px 18px -6px rgba(90, 60, 40, 0.35);
    text-align: center; color: var(--brown);
  }
  .offer-title { font-family: "Pacifico", cursive; font-size: 52px; line-height: 1; margin-top: 14px; height: 82px; }
  .offer-sub {
    font-family: "Fira Sans Condensed", sans-serif; font-weight: 700; color: var(--teal);
    font-size: 36px; letter-spacing: 2.5px; line-height: 1; margin-top: 14px;
  }
  .dotted-rule { width: 540px; margin: 18px auto 0; border-top: 6px dotted var(--brown); }
  .offer-body { font-family: "Bree Serif", serif; font-size: 30px; line-height: 40px; margin-top: 6px; }
  .offer-body sup { font-size: 17px; }
  .dotted-rule.bottom { margin-top: 8px; }

  .terms {
    position: absolute; left: 103px; top: 893px; width: 640px; text-align: center;
    font-family: "Fira Sans Condensed", sans-serif; font-weight: 600; font-size: 19px;
    line-height: 1.45; color: var(--ink);
  }

  .clinic-badge {
    position: absolute; left: 305px; top: 975px; width: 237px; height: 136px;
    background: var(--brown); display: flex; align-items: center; justify-content: center; gap: 12px;
  }
  .clinic-badge .dot { width: 22px; height: 22px; border-radius: 50%; background: var(--orange); }
  .clinic-badge .clinic-name {
    font-family: "Fredoka", sans-serif; font-weight: 600; font-size: 42px; color: var(--white);
  }

  .contact-bar {
    position: absolute; left: 0; top: 1140px; width: 846px; height: 60px; background: var(--orange);
    display: flex; align-items: center; justify-content: center; gap: 14px;
    font-family: "Fira Sans Condensed", sans-serif; font-weight: 700; font-size: 36px;
    letter-spacing: 1px; color: var(--white);
  }
  .contact-bar svg { width: 36px; height: 36px; }
</style>
</head>
<body>
<main class="poster">
  <div class="hero-photo" role="img" aria-label="Photo of a golden puppy nuzzling a grey kitten"></div>

  <div class="paper">
    <svg width="846" height="870" viewBox="0 0 846 870" role="img" aria-label="Pale paper backdrop with a soft pink paw print pattern">
      <defs>
        <linearGradient id="paperTone" x1="0" y1="0" x2="0" y2="1">
          <stop offset="0" stop-color="var(--paper)"/>
          <stop offset="0.5" stop-color="#f7e4e1"/>
          <stop offset="1" stop-color="var(--paw-pink)"/>
        </linearGradient>
      </defs>
      <polygon fill="url(#paperTone)" points="0,40 90,38 130,30 190,40 260,22 330,38 400,20 470,36 500,12 560,40 610,20 660,30 700,22 760,34 800,30 846,38 846,870 0,870"/>
    </svg>
  </div>

  <div class="voucher-tag">
    <div class="tag-pets" role="img" aria-label="Small cartoon dog and cat peeking over the tag"></div>
    <div class="tag-frame"></div>
    <div class="tag-body"><sup>$</sup>30 VOUCHER</div>
  </div>

  <h1>
    <span class="headline headline-we">WE</span>
    <svg class="heart" viewBox="0 0 100 90" aria-label="love">
      <path fill="var(--pink)" d="M50 88 C20 66 0 48 0 26 C0 10 12 0 27 0 C38 0 46 6 50 14 C54 6 62 0 73 0 C88 0 100 10 100 26 C100 48 80 66 50 88 Z"/>
    </svg>
    <span class="headline headline-name">PAL SPOTTERS!</span>
  </h1>

  <section class="offer-card">
    <h2 class="offer-title">Refer a fur friend</h2>
    <p class="offer-sub">TO OUR FRIENDLY TEAM</p>
    <div class="dotted-rule"></div>
    <p class="offer-body">and both your fur child and<br>their fur child will receive a<br><sup>$</sup>30 voucher to use in clinic! *</p>
    <div class="dotted-rule bottom"></div>
  </section>

  <p class="terms">* Limited to one pet per fur parent and the referred fur parent must be<br>new to our clinic. Unlimited vouchers for number of referrals!</p>

  <div class="clinic-badge">
    <span class="dot"></span>
    <span class="clinic-name">Vettoly</span>
  </div>

  <footer class="contact-bar">
    <svg viewBox="0 0 36 36" aria-hidden="true">
      <circle cx="18" cy="18" r="15" fill="none" stroke="var(--white)" stroke-width="2.5"/>
      <path fill="var(--white)" d="M13 10 l3 0 l1.5 4 l-2 1.5 c1 2.5 3 4.5 5.5 5.5 l1.5 -2 l4 1.5 l0 3 c0 1 -1 2 -2 2 c-7 -0.5 -12.5 -6 -13 -13 c0 -1 1 -2.5 1.5 -2.5 z"/>
    </svg>
    <span>(02) 5550 1942 | www.vettoly.com.au</span>
  </footer>
</main>
</body>
</html>
```